Tessel Vodka bottle label for grassroots distiller, micro-distiller in Kansas. Quillan Forge Distilli

We are located in South Central Kansas. Needing a design for a vodka label. The vodka will be distilled using white milo, which has not been done in the US as far as we know. We are in Kansas and a true "grass roots" business. We are starting on a shoestring, using bare essentials, and locally sourced components. We are looking for a clean, eye catching, grass roots feel. We also will be able to label it non gmo and Gluten free.

Target Market(s)

Upper mid-range price point. Target audience is professionals 25-50 with discretionary income and descerning taste.

Logo Text

Tessel Vodka, Sorghum Based Vodka. Non GMO, AND GLUTEN FREE. Quillan Forge Distilling, 847 W. 3rd Avenue, Kinsley, Ks.

Other font styles liked:
• Georgia, does not have to be, open

Colors
000000

Requirements
Must have
• Simple. Clean. And comply with PQX regulations for labeling found at www.PQX-regs.example
Nice to have
• Stylized image of White Milo. Proundly made in South Central Kansas with locally sourced grain.
Should not have
• Too many words. Exclusively Kansas.

```html
<!DOCTYPE html>
<html lang="en">
<head>
<meta charset="utf-8">
<title>Tessel Vodka — Bottle Label</title>
<link rel="stylesheet" href="https://fonts.googleapis.com/css2?family=Lora:wght@400;600;700&display=swap">
<style>
  :root {
    --backdrop: #111214;
    --label-paper: #e6e8eb;
    --pattern-tone: #d6d9dd;
    --ink: #111111;
    --plant-tone: #2a2a2a;
  }
  * { margin: 0; padding: 0; box-sizing: border-box; }
  html, body {
    width: 1200px;
    height: 1198px;
    overflow: hidden;
    background: var(--backdrop);
  }
  .canvas {
    position: relative;
    width: 1200px;
    height: 1198px;
  }
  .label {
    position: absolute;
    left: 440px;
    top: 360px;
    width: 300px;
    height: 700px;
    background: var(--label-paper);
    color: var(--ink);
    font-family: "Lora", Georgia, serif;
    overflow: hidden;
  }
  .label-pattern {
    position: absolute;
    left: 0; top: 0;
    width: 300px;
    height: 480px;
    background: linear-gradient(180deg, var(--pattern-tone), var(--label-paper));
  }
  .maker-mark {
    position: absolute;
    left: 0; width: 300px;
    top: 36px;
    display: flex;
    justify-content: center;
    align-items: center;
    gap: 8px;
    font-size: 22px;
    font-weight: 700;
    line-height: 30px;
  }
  .maker-mark .mark-square {
    width: 16px; height: 16px;
    background: var(--ink);
  }
  .brand-name {
    position: absolute;
    left: 0; width: 300px;
    top: 120px;
    text-align: center;
    font-size: 76px;
    font-weight: 700;
    line-height: 90px;
    letter-spacing: -1px;
  }
  .spirit-type {
    position: absolute;
    left: 210px;
    top: 343px;
    transform: translate(-50%, -50%) rotate(90deg);
    font-size: 84px;
    font-weight: 700;
    line-height: 1;
    white-space: nowrap;
  }
  .claims {
    position: absolute;
    left: 32px;
    top: 342px;
    transform: translate(-50%, -50%) rotate(-90deg);
    font-size: 29px;
    line-height: 1.02;
    text-align: center;
    white-space: nowrap;
  }
  .plant-art {
    position: absolute;
    left: 91px;
    top: 212px;
    width: 78px;
    height: 266px;
    border-radius: 50% 50% 40% 40% / 24% 24% 10% 10%;
    background: linear-gradient(180deg, var(--plant-tone), var(--ink));
  }
  .rule {
    position: absolute;
    left: 19px;
    top: 476px;
    width: 261px;
    height: 2px;
    background: var(--ink);
  }
  .detail {
    position: absolute;
    left: 0; width: 308px;
    text-align: center;
    font-size: 26px;
    line-height: 30px;
  }
  .detail.grain { top: 486px; }
  .detail.proof { top: 519px; }
  .volume-row {
    position: absolute;
    left: 2px;
    width: 290px;
    top: 552px;
    display: flex;
    justify-content: space-between;
    font-size: 23px;
    line-height: 28px;
  }
  .origin {
    position: absolute;
    left: 0; width: 308px;
    top: 610px;
    text-align: center;
    font-size: 22px;
    font-weight: 600;
    line-height: 29px;
  }
</style>
</head>
<body>
<main class="canvas">
  <section class="label">
    <div class="label-pattern" role="img" aria-label="Soft repeating fan-shaped pattern in pale grey across the upper label"></div>

    <div class="maker-mark">
      <span class="mark-square"></span>
      <span class="maker-name">Quillan Forge</span>
    </div>

    <h1 class="brand-name">Tessel</h1>
    <div class="spirit-type">Vodka</div>

    <div class="claims">NON GMO<br>GLUTEN FREE</div>

    <div class="plant-art" role="img" aria-label="Black silhouette illustration of a tall white sorghum plant"></div>

    <div class="rule"></div>

    <p class="detail grain">locally sourced grain</p>
    <p class="detail proof">80 Proof</p>

    <div class="volume-row">
      <span>750ml</span>
      <span>40%&nbsp; Alc/Vol</span>
    </div>

    <p class="origin">Proudly made in<br>South Central Kansas</p>
  </section>
</main>
</body>
</html>
```